Birchfield Vacation Rentals Bill Board

7x21 bill board.

Im needing a bill board for a vacation rental company. Specializing in cabin rentals.
Here are the main points I want mentioned on the billboard:

Quality vacation rentals

Accepting new vacation rental homes.

Family owned and operated.

Birchfieldvr.example
555-318-7042

Use either logo whichever looks best. Be creative

Target Market(s)

Cabin owners

Industry/Entity Type

Hospitality

Font styles to use
Sans Serif

Requirements
Must have
• Would like the cabin picture to be the background. Must have the birchfield logo, phone number and website

```html
<!DOCTYPE html>
<html lang="en">
<head>
<meta charset="utf-8">
<title>Birchfield Vacation Rentals Billboard</title>
<link rel="stylesheet" href="https://fonts.googleapis.com/css2?family=Montserrat:wght@400;500;600&display=swap">
<style>
  :root {
    --page: #e4e4e4;
    --ink: #2a2a2d;
    --panel-dark: #2e2e31;
    --paper: #ffffff;
    --light-text: #f2f2f2;
    --muted-line: #8a8a8e;
    --photo-sky: #b9cfd6;
    --photo-trees: #5f7a45;
    --photo-cabin: #2f3c40;
    --photo-wood: #7a4a2e;
  }
  html, body {
    margin: 0;
    width: 1200px;
    height: 1200px;
    overflow: hidden;
    background: var(--page);
    font-family: "Montserrat", sans-serif;
  }
  .billboard {
    position: absolute;
    left: 0;
    top: 400px;
    width: 1200px;
    height: 400px;
    overflow: hidden;
  }
  .billboard-shapes {
    position: absolute;
    inset: 0;
  }
  .brand {
    position: absolute;
    left: 30px;
    top: 150px;
    color: var(--ink);
  }
  .brand-name {
    display: flex;
    align-items: center;
    gap: 12px;
    font-size: 33px;
    font-weight: 600;
    letter-spacing: -0.5px;
    margin: 0;
  }
  .brand-mark {
    width: 16px;
    height: 16px;
    background: var(--ink);
  }
  .brand-web {
    font-size: 17px;
    font-weight: 500;
    margin: 8px 0 0 0;
  }
  .brand-phone {
    font-size: 24px;
    font-weight: 500;
    margin: 28px 0 0 0;
  }
  .brand-tagline {
    font-size: 14px;
    font-weight: 500;
    letter-spacing: 0.5px;
    margin: 18px 0 0 0;
  }
  .pitch {
    position: absolute;
    left: 720px;
    top: 0;
    width: 480px;
    height: 400px;
    color: var(--light-text);
    text-align: center;
  }
  .pitch-headline {
    position: absolute;
    left: 0;
    right: 0;
    top: 82px;
    margin: 0;
    font-size: 54px;
    font-weight: 400;
    line-height: 1.12;
  }
  .pitch-rule {
    position: absolute;
    left: 70px;
    right: 60px;
    top: 292px;
    height: 1px;
    background: var(--muted-line);
  }
  .pitch-copy {
    position: absolute;
    left: 40px;
    right: 20px;
    top: 312px;
    margin: 0;
    font-size: 14px;
    line-height: 1.6;
  }
</style>
</head>
<body>
  <section class="billboard">
    <svg class="billboard-shapes" width="1200" height="400" viewBox="0 0 1200 400">
      <defs>
        <linearGradient id="cabin-photo" x1="0" y1="0" x2="0" y2="1">
          <stop offset="0" stop-color="var(--photo-sky)"/>
          <stop offset="0.25" stop-color="var(--photo-trees)"/>
          <stop offset="0.55" stop-color="var(--photo-cabin)"/>
          <stop offset="0.85" stop-color="var(--photo-wood)"/>
          <stop offset="1" stop-color="var(--photo-trees)"/>
        </linearGradient>
      </defs>
      <rect class="cabin-photo" x="250" y="0" width="520" height="400" fill="url(#cabin-photo)" role="img" aria-label="Photo of a dark-sided wooden cabin with a covered front porch among tall trees"/>
      <polygon class="paper-panel" points="0,0 270,0 400,400 0,400" fill="var(--paper)"/>
      <polygon class="accent-wedge" points="270,0 350,0 308,118" fill="var(--panel-dark)"/>
      <polygon class="dark-panel" points="765,0 1200,0 1200,400 712,400 652,210" fill="var(--panel-dark)"/>
      <g class="social-marks" fill="var(--light-text)">
        <rect x="800" y="34" width="12" height="16" rx="2"/>
        <rect x="818" y="34" width="16" height="16" rx="2"/>
        <circle cx="846" cy="42" r="8"/>
        <circle cx="866" cy="42" r="7"/>
        <rect x="914" y="28" width="1" height="28"/>
        <rect x="950" y="32" width="30" height="18" rx="3"/>
        <circle cx="998" cy="41" r="10"/>
        <circle cx="1022" cy="41" r="10"/>
        <rect x="1042" y="32" width="34" height="18" rx="3"/>
      </g>
    </svg>

    <div class="brand">
      <p class="brand-name"><span class="brand-mark"></span>BIRCHFIELDVR</p>
      <p class="brand-web">Birchfieldvr.example</p>
      <p class="brand-phone">555-318-7042</p>
      <p class="brand-tagline">CABIN STAYS MADE SIMPLE</p>
    </div>

    <div class="pitch">
      <h1 class="pitch-headline">QUALITY<br>VACATION<br>RENTALS</h1>
      <div class="pitch-rule"></div>
      <p class="pitch-copy">Accepting new vacation rental homes.<br>Family owned and operated.</p>
    </div>
  </section>
</body>
</html>
```